Brett Olsen Building Business Card Design

Hi,

I need a business card for my Building company.
I am a Builder and build homes for clients.
I am looking for a sophisticated logo that can be used on business cards, envelopes and letter heads.
I am trying to take my business to the next level and need a professional business card.

Colours: Please use white, black, dark grey and bright blue.

Thank you,

Carol and Brett.

Target Market(s)

1. Home and Building Companies 2. Potential customers

Industry/Entity Type

Business

Contact Information for Business Card

Brett Olsen Building PTY LTD

Brett Olsen

Director

A.B.N. 37 829 516 073

BUILDERS LICENCE No. 573019k

Mobile: 0412 907 381

Email: brettolsenbuilding@mailvane.com.au

Requirements
Must have
• The following is compulsory to have in the designs:

Brett Olsen Building PTY LTD (business name)

Brett Olsen (contact name)

Director (position)

A.B.N. 37 829 516 073

Builders Licence No. 573019k

Mobile: 0412 907 381

Nice to have
• Logo for business
Should not have
• Should not be cluttered.

I am looking for a clean, sophisticated and professional business card design.

```html
<!DOCTYPE html>
<html lang="en">
<head>
<meta charset="utf-8">
<title>Brett Olsen Building – Business Card</title>
<link rel="stylesheet" href="https://fonts.googleapis.com/css2?family=Roboto+Condensed:wght@400&display=swap">
<style>
  :root {
    --canvas: #ffffff;
    --card-dark: #6d6e71;
    --card-light: #e0e1e2;
    --name-light: #bcbdc0;
    --name-dark: #87888c;
    --text: #77787b;
  }
  * { margin: 0; padding: 0; box-sizing: border-box; }
  html, body {
    width: 1200px;
    height: 1000px;
    overflow: hidden;
    background: var(--canvas);
    font-family: "Roboto Condensed", "Arial Narrow", sans-serif;
  }
  .canvas { position: relative; width: 1200px; height: 1000px; }

  .card { position: absolute; }
  .card--front {
    left: 210px; top: 33px; width: 780px; height: 448px;
    background: var(--card-dark);
    display: flex; align-items: center; justify-content: center;
  }
  .card--back {
    left: 211px; top: 517px; width: 779px; height: 447px;
    background: var(--card-light);
  }

  .brand-name {
    font-weight: 400;
    white-space: nowrap;
    line-height: 1;
  }
  .card--front .brand-name {
    color: var(--name-light);
    font-size: 62px;
  }
  .card--back .brand-name {
    position: absolute;
    left: 52px; top: 98px;
    color: var(--name-dark);
    font-size: 28px;
  }

  .contact {
    position: absolute;
    left: 248px; top: 215px;
    list-style: none;
    color: var(--text);
    font-size: 25px;
    line-height: 33px;
  }
</style>
</head>
<body>
  <main class="canvas">
    <section class="card card--front" aria-label="Card front">
      <p class="brand-name">Brett Olsen Building</p>
    </section>

    <section class="card card--back" aria-label="Card back">
      <p class="brand-name">Brett Olsen Building</p>
      <ul class="contact">
        <li>Brett Olsen Building PTY LTD</li>
        <li>Brett Olsen Director</li>
        <li>A.B.N. 37 829 516 073</li>
        <li>BUILDERS LICENCE No. 573019k</li>
        <li>Mobile: 0412 907 381</li>
        <li>Email: brettolsenbuilding@mailvane.com.au</li>
      </ul>
    </section>
  </main>
</body>
</html>
```